Marlo's Pizzeria BOGO Promotion Pizza Flyer (Huron)

Pizzeria flyer promoting "under new management" and then the main point for this flyer is our Buy One Get One Free promotion on our pizzas (disclaimer: not valid for Mini Feast Tray or Crowd Pies)(we reserve the right to cancel this promotion at any time)
This promotion has no limit and can be carryout or delivery. No coupon needed.
Looking for a fun bright flyer with our logo colors

Requirements
Must have
• Store Info
• 287 Wexford Rd. E
• Huron, OH
• 419-867-2093
• Open at 4pm Daily!

```html
<!DOCTYPE html>
<html lang="en">
<head>
<meta charset="utf-8">
<title>Marlo's Pizzeria BOGO Flyer</title>
<link rel="stylesheet" href="https://fonts.googleapis.com/css2?family=Montserrat:wght@500;600;700;800;900&display=swap">
<style>
  :root {
    --backdrop: #2a2726;
    --ink-black: #141414;
    --ink-black-soft: #222;
    --sauce-red: #c8151b;
    --sauce-red-deep: #7e0a0e;
    --pill-red: #b5141a;
    --cheese-yellow: #ffd21f;
    --white: #ffffff;
    --plate: #f3f1ee;
  }
  * { margin: 0; padding: 0; box-sizing: border-box; }
  html, body { width: 1200px; height: 900px; overflow: hidden; }
  body {
    background: var(--backdrop);
    font-family: "Montserrat", sans-serif;
    position: relative;
  }
  .flyer {
    position: absolute;
    left: 317px; top: 40px;
    width: 566px; height: 820px;
    overflow: hidden;
    background: radial-gradient(ellipse at 50% 20%, var(--ink-black-soft), var(--ink-black) 70%);
  }
  .flyer-art { position: absolute; inset: 0; }
  .brand {
    position: absolute; left: 20px; top: 34px;
    display: flex; align-items: center; gap: 8px;
    color: var(--white);
    font-weight: 800; font-size: 15px; line-height: 1.1;
    width: 130px;
  }
  .brand-dot {
    flex: none; width: 22px; height: 22px; border-radius: 50%;
    background: var(--sauce-red);
  }
  .top-call {
    position: absolute; right: 20px; top: 30px;
    color: var(--white); font-weight: 600; font-size: 13px; letter-spacing: 0.5px;
  }
  .headline {
    position: absolute; left: 0; right: 0; top: 118px;
    display: flex; justify-content: center; align-items: center; gap: 10px;
    padding-left: 10px;
  }
  .headline-stack {
    display: flex; flex-direction: column; font-weight: 800; font-size: 30px; line-height: 0.95;
  }
  .headline-stack .buy { color: var(--sauce-red); }
  .headline-stack .get { color: var(--white); }
  .headline-big { font-weight: 800; font-size: 80px; line-height: 1; letter-spacing: -1px; }
  .headline-big .one { color: var(--white); }
  .headline-big .free { color: var(--sauce-red); }
  .disclaimer {
    position: absolute; left: 93px; top: 199px; width: 380px; height: 45px;
    border-radius: 23px; background: var(--pill-red);
    color: var(--white); font-size: 11px; font-weight: 500; line-height: 1.35;
    display: flex; flex-direction: column; justify-content: center; align-items: center;
    text-align: center;
  }
  .contact {
    position: absolute; left: 0; right: 0; top: 668px;
    text-align: center; color: var(--white);
  }
  .contact-label { font-weight: 800; font-size: 21px; letter-spacing: 0.5px; }
  .contact-phone { color: var(--cheese-yellow); font-weight: 800; font-size: 38px; line-height: 1.15; }
  .contact-rule {
    width: 230px; margin: 6px auto 12px; border-top: 3px dotted var(--cheese-yellow);
  }
  .contact-line { font-size: 12.5px; font-weight: 600; letter-spacing: 1px; line-height: 2; }
</style>
</head>
<body>
  <main class="flyer">
    <svg class="flyer-art" width="566" height="820" viewBox="0 0 566 820">
      <defs>
        <radialGradient id="redField" cx="50%" cy="45%" r="70%">
          <stop offset="0" stop-color="var(--sauce-red)"/>
          <stop offset="1" stop-color="var(--sauce-red-deep)"/>
        </radialGradient>
        <radialGradient id="pizzaTones" cx="50%" cy="50%" r="50%">
          <stop offset="0" stop-color="#e7a85a"/>
          <stop offset="0.75" stop-color="#c9662c"/>
          <stop offset="1" stop-color="#a4451c"/>
        </radialGradient>
      </defs>
      <path class="red-field" d="M0 270 C60 262 90 300 150 305 C210 310 230 290 285 300 C360 312 420 245 490 255 C530 260 555 250 566 245 L566 820 L0 820 Z" fill="url(#redField)"/>
      <g class="side-dish-left" role="img" aria-label="Photo of a pizza on a plate">
        <circle cx="30" cy="454" r="68" fill="var(--plate)"/>
        <circle cx="30" cy="454" r="56" fill="url(#pizzaTones)"/>
      </g>
      <g class="side-dish-right" role="img" aria-label="Photo of a pizza on a plate">
        <circle cx="530" cy="415" r="62" fill="var(--plate)"/>
        <circle cx="530" cy="415" r="51" fill="url(#pizzaTones)"/>
      </g>
      <g class="hero-pizza" role="img" aria-label="Photo of a loaded pepperoni and vegetable pizza on a white plate">
        <circle cx="281" cy="463" r="158" fill="var(--plate)"/>
        <circle cx="281" cy="463" r="142" fill="url(#pizzaTones)"/>
      </g>
    </svg>

    <div class="brand"><span class="brand-dot"></span><span>Marlo's Pizzeria</span></div>
    <div class="top-call">E CALL 419 555 0148</div>

    <h1 class="headline">
      <span class="headline-stack"><span class="buy">BUY</span><span class="get">GET</span></span>
      <span class="headline-big"><span class="one">1</span> <span class="free">FREE</span></span>
    </h1>

    <p class="disclaimer">
      <span>Disclaimer: not valid for Mini Feast Tray or Crowd Pies</span>
      <span>we reserve the right to cancel this promotion at any time</span>
    </p>

    <section class="contact">
      <div class="contact-label">CALL NOW</div>
      <div class="contact-phone">+419-867-2093</div>
      <div class="contact-rule"></div>
      <div class="contact-line">OPENING HOUR : 4PM | PHONE CALL 419 555 0148</div>
      <div class="contact-line">287 WEXFORD RD. E- HURON, OH</div>
    </section>
  </main>
</body>
</html>
```